Brantmoor Financial Coaching LLC - Needed clean black business card

Business card for personal financial coaching practice located on Las Vegas NV, new startup. Back of card needs to have "how it works" to match the website.

Font styles to use
Sans Serif

Colors

Designer to choose colors to be used in the design.

```html
<!DOCTYPE html>
<html lang="en">
<head>
<meta charset="utf-8">
<title>Brantmoor Financial Coaching LLC – Business Card</title>
<link rel="stylesheet" href="https://fonts.googleapis.com/css2?family=Montserrat:wght@400;500;700;800&display=swap">
<style>
  :root {
    --backdrop: #262626;
    --card: #0e0e0e;
    --ink: #ffffff;
    --ink-soft: #e6e6e6;
    --rule: #cfcfcf;
  }
  * { margin: 0; padding: 0; box-sizing: border-box; }
  html, body { width: 1200px; height: 852px; overflow: hidden; }
  body {
    background: var(--backdrop);
    font-family: "Montserrat", Arial, sans-serif;
    color: var(--ink);
    position: relative;
  }
  .card {
    position: absolute;
    width: 540px;
    height: 309px;
    background: var(--card);
    border-radius: 18px;
    box-shadow: 0 14px 30px rgba(0,0,0,.45);
  }
  .card--back { left: 30px; top: 110px; }
  .card--front { left: 630px; top: 433px; }

  .brand-name {
    font-weight: 800;
    font-size: 21px;
    letter-spacing: .2px;
    color: var(--ink);
    white-space: nowrap;
  }

  /* Back side */
  .card--back { text-align: center; padding: 40px 44px 0; }
  .card--back .brand-name { display: block; }
  .section-title {
    margin-top: 26px;
    font-weight: 800;
    font-size: 17px;
    display: inline-block;
    position: relative;
    padding: 0 8px 8px;
  }
  .section-title__rule {
    display: block;
    width: 150px;
    height: 10px;
    margin: 0 auto 18px;
  }
  .process-text {
    font-size: 10.5px;
    line-height: 1.95;
    letter-spacing: .5px;
    color: var(--ink-soft);
  }
  .process-link {
    display: block;
    font-weight: 700;
    color: var(--ink);
    letter-spacing: .6px;
  }

  /* Front side */
  .card--front .brand-name { position: absolute; left: 38px; top: 44px; }
  .person { position: absolute; left: 38px; top: 168px; }
  .person__name { font-weight: 800; font-size: 21px; letter-spacing: .3px; }
  .person__role { font-size: 14px; font-weight: 400; margin-top: 2px; }
  .person__dash { width: 12px; height: 2px; background: var(--ink); margin: 10px 0 8px; }
  .person__address { font-style: normal; font-size: 13px; line-height: 1.35; }
  .contacts {
    position: absolute;
    left: 270px;
    top: 170px;
    list-style: none;
    font-size: 12.5px;
    line-height: 1;
  }
  .contacts li { display: flex; align-items: center; gap: 8px; margin-bottom: 12px; }
  .contacts svg { width: 12px; height: 12px; flex: none; fill: var(--ink); }
</style>
</head>
<body>

<section class="card card--back" aria-label="Card back">
  <span class="brand-name">Brantmoor Financial Coaching LLC</span>
  <h2 class="section-title">How It Works</h2>
  <svg class="section-title__rule" viewBox="0 0 150 10" aria-hidden="true">
    <line x1="0" y1="5" x2="150" y2="5" stroke="var(--rule)" stroke-width="1"/>
    <circle cx="75" cy="5" r="3" fill="var(--ink)"/>
  </svg>
  <p class="process-text">
    All free one-time consultations are in-person meetings only. Paid appointments
    may be scheduled for in-person or virtual meetings. Select the session, date and
    time that works best for your schedule. Start your journey of financial freedom at
    <span class="process-link">brantmoorcoaching.com</span>
  </p>
</section>

<section class="card card--front" aria-label="Card front">
  <span class="brand-name">Brantmoor Financial Coaching LLC</span>

  <div class="person">
    <h1 class="person__name">Marcus Halvorsen</h1>
    <p class="person__role">Manager</p>
    <div class="person__dash"></div>
    <address class="person__address">4120 W Sahara Ave #305-B<br>Las Vegas, NV 89102</address>
  </div>

  <ul class="contacts">
    <li>
      <svg viewBox="0 0 24 24" aria-hidden="true"><path d="M6.6 10.8a15.1 15.1 0 0 0 6.6 6.6l2.2-2.2a1 1 0 0 1 1-.25 11.4 11.4 0 0 0 3.6.57 1 1 0 0 1 1 1V20a1 1 0 0 1-1 1A17 17 0 0 1 3 4a1 1 0 0 1 1-1h3.5a1 1 0 0 1 1 1c0 1.25.2 2.45.57 3.57a1 1 0 0 1-.25 1z"/></svg>
      702-555-0147
    </li>
    <li>
      <svg viewBox="0 0 24 24" aria-hidden="true"><path d="M2 5h20v14H2zm2 2v.5l8 5 8-5V7zm0 2.8V17h16V9.8l-8 5z"/></svg>
      marcus@brantmoorcoaching.com
    </li>
    <li>
      <svg viewBox="0 0 24 24" aria-hidden="true"><path d="M12 2a10 10 0 1 0 0 20 10 10 0 0 0 0-20zm6.9 6h-3a15.7 15.7 0 0 0-1.3-3.9A8 8 0 0 1 18.9 8zM12 4c.8 1.2 1.5 2.5 1.9 4h-3.8c.4-1.5 1.1-2.8 1.9-4zM4.3 14a8.2 8.2 0 0 1 0-4h3.4a16.5 16.5 0 0 0 0 4zm.8 2h3a15.7 15.7 0 0 0 1.3 3.9A8 8 0 0 1 5.1 16zm3-8h-3a8 8 0 0 1 4.3-3.9A15.7 15.7 0 0 0 8.1 8zM12 20c-.8-1.2-1.5-2.5-1.9-4h3.8c-.4 1.5-1.1 2.8-1.9 4zm2.3-6H9.7a14.7 14.7 0 0 1 0-4h4.6a14.7 14.7 0 0 1 0 4zm.3 5.9a15.7 15.7 0 0 0 1.3-3.9h3a8 8 0 0 1-4.3 3.9zm1.7-5.9a16.5 16.5 0 0 0 0-4h3.4a8.2 8.2 0 0 1 0 4z"/></svg>
      www.brantmoorcoaching.com
    </li>
  </ul>
</section>

</body>
</html>
```